RM Tomás Ferrier (Business Card)

Hi designers, in this work, I'm looking for an sophisticated stylish, elegant and proffesional personal card. We have a laboratory of pathology automated, with equipments high quality.
In this web the designers, have created my business logo, the name is "RM Tomás Ferrier"
In our lab, we principal work is to prepare the biopsies for further diagnostic of diseases like cancer, tumors, etc.
I need that the first face, only having my complete logo (Rm Tomás Ferrier, Laboratorio de procesamiento Histologico)
The overleaf, could repeat the same logo, like water logo.
In this face, I need to say: My full data:

Técnico en Anatomía Patológica
Tomás Ferrier Bustos M.P 48207
Av. Ramón Quiroga 817 - 2do piso - Instituto Brandeck.
Córdoba, Argentina
(0351) 156284930
ferrier.tomas@correoluz.com

with respect the colors of card, use your imagination, the original logo color is violet, I haven't chosen a color base for the card.

attached pictures are examples of cards I like your DESIGN.
Attached too, the original logo to my company.

the size of card are:
horizontal: 9cm
vertical: 5,5cm

any question that you have, not doubt to question me,
Hand to work!

Industry/Entity Type

Laboratory

Requirements
Must have
• designers sophisticated, not simples, like show the images attached

```html
<!DOCTYPE html>
<html lang="es">
<head>
<meta charset="utf-8">
<title>Tomás Ferrier — Tarjeta personal</title>
<link rel="stylesheet" href="https://fonts.googleapis.com/css2?family=Montserrat:wght@400;600;700&family=Open+Sans:ital,wght@0,400;0,600;0,700;1,400&family=Oswald:wght@400;500&display=swap">
<style>
  :root {
    --stage: #000000;
    --card: #ffffff;
    --violet: #6b2f96;
    --violet-soft: #c9b6dc;
    --grey: #88898c;
    --grey-dark: #5e5f62;
    --grey-soft: #d6d6d8;
  }
  html, body {
    margin: 0;
    padding: 0;
    width: 1200px;
    height: 575px;
    overflow: hidden;
    background: var(--stage);
  }
  .stage {
    position: relative;
    width: 1200px;
    height: 575px;
  }
  .card {
    position: absolute;
    top: 159px;
    width: 433px;
    height: 262px;
    border-radius: 20px;
    overflow: hidden;
    background: var(--card);
  }
  .card svg { display: block; width: 100%; height: 100%; }
  .card--front { left: 124px; }
  .card--back { left: 637px; }

  .logo-name {
    font-family: "Montserrat", sans-serif;
    font-weight: 600;
    font-size: 9px;
    letter-spacing: 2.6px;
    fill: var(--grey);
  }
  .logo-tagline {
    font-family: "Oswald", sans-serif;
    font-weight: 400;
    font-size: 9.4px;
    fill: var(--grey-dark);
  }
  .watermark {
    font-family: "Montserrat", sans-serif;
    font-weight: 700;
    font-size: 17px;
    fill: var(--violet-soft);
    opacity: 0.55;
  }
  .role {
    font-family: "Open Sans", sans-serif;
    font-weight: 600;
    font-size: 7.2px;
    fill: var(--violet);
  }
  .holder {
    font-family: "Open Sans", sans-serif;
    font-weight: 700;
    font-size: 6.6px;
    fill: var(--grey-dark);
  }
  .holder .registration {
    font-weight: 400;
    font-style: italic;
    font-size: 5.2px;
    fill: var(--grey);
  }
  .contact {
    font-family: "Open Sans", sans-serif;
    font-weight: 400;
    font-size: 6.6px;
    fill: var(--grey-dark);
  }
  .address {
    font-family: "Open Sans", sans-serif;
    font-weight: 400;
    font-size: 6.6px;
    fill: #ffffff;
  }
</style>
</head>
<body>
<main class="stage">

  <section class="card card--front" aria-label="Frente de la tarjeta">
    <svg viewBox="0 0 256 155" xmlns="http://www.w3.org/2000/svg">
      <rect class="card-base" width="256" height="155" fill="var(--card)"/>
      <polygon class="corner corner--violet" points="0,0 50,0 14,78 46,155 0,155" fill="var(--violet)"/>
      <polygon class="corner corner--grey" points="196,0 256,0 256,155 206,155 242,78" fill="var(--grey)"/>
      <polygon class="panel" points="50,0 196,0 242,78 206,155 46,155 14,78" fill="var(--card)"/>
      <polyline class="bracket bracket--grey" points="58,12 24,78 58,143" fill="none" stroke="var(--grey)" stroke-width="4"/>
      <line class="rule rule--grey" x1="58" y1="12" x2="150" y2="12" stroke="var(--grey)" stroke-width="4"/>
      <polyline class="bracket bracket--violet" points="168,12 198,12 232,78 198,143 168,143" fill="none" stroke="var(--violet)" stroke-width="4"/>
      <line class="rule rule--grey" x1="58" y1="143" x2="110" y2="143" stroke="var(--grey)" stroke-width="4"/>

      <text class="logo-name" x="128" y="72" text-anchor="middle">RM TOMÁS FERRIER</text>
      <line x1="62" y1="78" x2="194" y2="78" stroke="var(--grey-soft)" stroke-width="0.6"/>
      <text class="logo-tagline" x="128" y="91" text-anchor="middle">LABORATORIO DE PROCESAMIENTO HISTOLOGICO</text>
    </svg>
  </section>

  <section class="card card--back" aria-label="Dorso de la tarjeta">
    <svg viewBox="0 0 256 155" xmlns="http://www.w3.org/2000/svg">
      <rect class="card-base" width="256" height="155" fill="var(--card)"/>
      <text class="watermark" x="8" y="24">RM Tomás</text>
      <text class="watermark" x="8" y="44">Ferrier</text>

      <text class="role" x="241" y="36" text-anchor="end">Técnico en Anatomía Patológica</text>
      <text class="holder" x="241" y="47" text-anchor="end">Tomás Ferrier Bustos <tspan class="registration">M.P 48207</tspan></text>

      <text class="contact" x="224" y="80" text-anchor="end">(0351) 156284930</text>
      <g class="icon icon--phone" transform="translate(233 77.8)">
        <circle r="4" fill="var(--violet)"/>
        <path d="M-1.8,-2.2 q-0.8,2.6 1.6,4.4 l0.9,-0.9 l1.3,0.8 l-0.6,1 q-3.4,-0.6 -4.2,-4.5 z" fill="#ffffff"/>
      </g>
      <text class="contact" x="224" y="96" text-anchor="end">ferrier.tomas@correoluz.com</text>
      <g class="icon icon--mail" transform="translate(233 93.8)">
        <circle r="4" fill="var(--violet)"/>
        <rect x="-2.3" y="-1.6" width="4.6" height="3.2" fill="none" stroke="#ffffff" stroke-width="0.6"/>
        <polyline points="-2.3,-1.6 0,0.4 2.3,-1.6" fill="none" stroke="#ffffff" stroke-width="0.6"/>
      </g>

      <rect class="address-band" x="0" y="119" width="256" height="36" fill="var(--violet)"/>
      <text class="address" x="128" y="135" text-anchor="middle">Av. Ramón Quiroga 817 - 2do piso - Instituto Brandeck.</text>
      <text class="address" x="128" y="146" text-anchor="middle">Córdoba, Argentina</text>
    </svg>
  </section>

</main>
</body>
</html>
```